Brochure Design Project

We are a payroll company. We offer a wide variety of products and services:
1. Payroll Processing
2. Employee Direct Deposit
3. Time and attendance
4. HR services
5. Employee Employee Benefits

I'd like to develop a one page template that uses a combination of our logo (attached), colors (attached) and possible a picture. The picture could be shown as an option as it may change based on the product or service.

Target Market(s)

Adults in the United States ages 22-50. Typically these people are accountants, human resource professionals or entrepreneurs. The payroll industry is dominated by 3 large payroll processors, QLM, Wendrafy and Tolvarex. These companies are very impersonal and make it difficult to resolve issues when they arise. We have grown to over 400 clients by being the opposite of the big guys,

Industry/Entity Type

It Company

Font styles to use
Sans Serif

Requirements
Must have
• The brochure can be one or two pages.
Nice to have
• I'll know it when I see it but I can't describe it. I have attached a few brochures that have caught my eye.
Should not have
• No cartoons. No money signs. Hip, new, fresh are words I'd use to describe the winning product. Of the three people I described in my target market, the entrepreneur is the market I'd most like to target.

```html
<!DOCTYPE html>
<html lang="en">
<head>
<meta charset="utf-8">
<title>Ledgerly Works — Service Flyer</title>
<link rel="stylesheet" href="https://fonts.googleapis.com/css2?family=Oxygen:wght@400;700&display=swap">
<style>
:root{
  --navy:#2b3a7a;
  --navy-deep:#1f2b63;
  --blue-band:#34468c;
  --green:#8cc63f;
  --green-soft:#dcecc6;
  --ink:#27336b;
  --grey:#6b6f78;
  --paper:#ffffff;
  --backdrop:#ecebe8;
}
*{box-sizing:border-box;margin:0;padding:0}
html,body{width:1200px;height:813px;overflow:hidden}
body{background:var(--backdrop);font-family:'Oxygen',sans-serif;color:var(--ink);position:relative}
.page{position:absolute;top:96px;width:480px;height:620px;background:var(--paper);box-shadow:0 6px 18px rgba(0,0,0,.18);overflow:hidden}
.page--front{left:60px}
.page--back{left:660px}

/* brand name */
.brand{display:flex;align-items:center;gap:8px;font-weight:700;color:var(--navy);font-size:20px}
.brand__dot{width:12px;height:12px;border-radius:50%;background:var(--green)}

/* front page */
.front__header{position:absolute;top:50px;left:34px;right:30px;display:flex;justify-content:space-between;align-items:flex-end;border-bottom:1px solid #cfd2d8;padding-bottom:10px}
.tagline{font-size:11px;letter-spacing:1.5px;color:var(--grey)}
.front__band{position:absolute;top:110px;left:0;width:480px;height:190px}
.front__intro{position:absolute;top:150px;left:34px;right:34px;color:#fff;font-size:14px;line-height:1.45;text-align:justify}
.front__photo{position:absolute;top:270px;left:262px;width:190px;height:110px;background:linear-gradient(135deg,#dfe6ef 0%,#9aa9c2 55%,#2d3a6b 100%)}
.service-list{position:absolute;top:352px;left:34px;width:220px;list-style:none}
.service-list li{font-weight:700;font-size:16px;color:var(--navy-deep);padding:6px 0;border-bottom:1px solid var(--green)}
.service-list li:last-child{border-bottom:none}
.front__rule{position:absolute;top:470px;left:34px;right:30px;border-top:1px solid var(--green)}
.front__outro{position:absolute;top:484px;left:34px;right:30px;font-size:11.5px;line-height:1.55;color:var(--ink)}

/* back page */
.back__swoosh{position:absolute;top:0;left:0;width:480px;height:130px}
.back__tagline{position:absolute;top:52px;right:26px;font-size:17px;letter-spacing:.5px;color:var(--grey)}
.back__lead{position:absolute;top:132px;left:34px;right:30px;border-top:1px solid var(--green);padding-top:8px}
.section-title{font-weight:700;font-size:15px;color:var(--navy-deep);margin-bottom:6px}
.copy{font-size:11px;line-height:1.5;color:var(--ink)}
.back__cols{position:absolute;top:236px;left:34px;right:30px;display:flex;gap:26px}
.back__cols>div{flex:1}
.back__cols .section-title{border-bottom:1px solid var(--green);padding-bottom:4px}
.back__closing{position:absolute;top:400px;left:34px;right:30px;font-size:12px;font-style:italic;color:var(--ink);line-height:1.5}
.back__brand{position:absolute;top:452px;right:30px}
.back__footer{position:absolute;bottom:0;left:0;width:480px;height:120px;background:linear-gradient(180deg,var(--blue-band),var(--navy-deep));color:#fff;padding:26px 34px;font-size:10.5px;line-height:1.5}
</style>
</head>
<body>

<section class="page page--front">
  <header class="front__header">
    <div class="brand"><span class="brand__dot"></span>Ledgerly Works</div>
    <span class="tagline">Innovative solutions that deliver value</span>
  </header>

  <svg class="front__band" viewBox="0 0 480 190" aria-hidden="true">
    <polygon points="0,8 480,0 480,170 0,185" fill="#b9bdc6"/>
    <polygon points="0,12 480,4 480,164 0,178" fill="var(--blue-band)"/>
  </svg>
  <p class="front__intro">Ledgerly Works offers exceptional payroll management services. Accurate and timely payroll managment is a basic requirement of every business. Utilize your resources better by partnering with Ledgerly Works.</p>

  <div class="front__photo" role="img" aria-label="Photo of a business team working together at a desk"></div>

  <ul class="service-list">
    <li>HR services</li>
    <li>Payroll Processing</li>
    <li>Time and attendance</li>
  </ul>

  <div class="front__rule"></div>
  <p class="front__outro">As your business evolves, we work along side you to reasses your options and make suggestions to improve your business efficacy. Allow us to handle your payroll management and give yourself more time to manage your business!</p>
</section>

<section class="page page--back">
  <svg class="back__swoosh" viewBox="0 0 480 130" aria-hidden="true">
    <path d="M0,110 C140,70 300,30 480,0 L480,0 L0,0 Z" fill="#fff"/>
    <path d="M0,120 C160,60 320,20 480,6 L480,30 C330,42 170,84 0,130 Z" fill="var(--green-soft)"/>
    <path d="M0,96 C170,58 330,34 480,0 L480,20 C330,48 170,80 0,112 Z" fill="var(--green)"/>
  </svg>
  <p class="back__tagline">Innovative solutions that deliver value</p>

  <div class="back__lead">
    <h2 class="section-title">Payroll Processing</h2>
    <p class="copy">Streamline payroll processing services for you and your employees with Ledgerly Works. Give your employees all the options of a large corporation, no matter the size of your business. We'll guide you through the process of choosing the services that make sense for your company, at a price you can afford!</p>
  </div>

  <div class="back__cols">
    <div>
      <h2 class="section-title">HR services</h2>
      <p class="copy">Ledgerly Works provides a customized approach and comprehensive set of HR Solutions for your business.<br>Our services are designed to help businesses minimize risk, save money, and eliminate the hassle of managing employee services.</p>
    </div>
    <div>
      <h2 class="section-title">Employee Benefits</h2>
      <p class="copy">A comprehensive benefits administration program is important when it comes to hiring and retaining quality employees. Benefits Administration is a complex task and can be taxing on your staff. Ledgerly Works offers a seemless way to manage this for your business.</p>
    </div>
  </div>

  <p class="back__closing">Ensure your employees give you their best work by providing them with integrated employer solutions you can count on.</p>

  <div class="brand back__brand"><span class="brand__dot"></span>Ledgerly Works</div>

  <footer class="back__footer">
    <address style="font-style:normal">
      Ledgerly Works, Inc.<br>
      88 North Mill Road | Suite 12, Dover PA, 19000<br>
      Tel: 555 010 2200 | Fax: 555 010 2201<br>
      E-mail: jdoe@ledgerlyworks.com<br>
      Web: http://www.ledgerlyworks.com
    </address>
  </footer>
</section>

</body>
</html>
```